Quillmark Letterpress Printing needs a "poster" for Vending Machine to sell mini-letterp...

I am a letterpress printer and have just purchased a small vending machine to take to craft markets/local boutiques and sell Mini-Letterpress Prints for $1 (four quarters).  Here is a link to what the machine looks like:  https://www.treatvendco.example/Heron-Decal-and-Stamp-Vending-Unit-Q4817.aspx
I need you all to design fun artwork for the front of the machine... dimensions are:  18" height, 15" width.  My company website is Quillmarkletterpress.example if you want to see my branding.  The mini-prints will constantly be changing, and each will be signed (by me).  I would like a strong "letterpress" look.... old school Brindle Yard Press type vibe.  I want it to look fun, colorful, and capture many impulse purchases.

Target Market(s)
impulse purchasers at artisan craft markets and small high end boutique stores
Requirements
Must have
- would prefer the colors to coordinate and/or mostly match my brand

Nice to have
- I would like to have a manicule on the design.... maybe: 4 quarters [manicule] 1 surprise print

Should not have
- comic sans

```html
<!DOCTYPE html>
<html lang="en">
<head>
<meta charset="utf-8">
<title>Mini Letterpress Vending Prints Machine — Quillmark Letterpress Printing</title>
<link rel="stylesheet" href="https://fonts.googleapis.com/css2?family=Anton&family=Alfa+Slab+One&family=Archivo+Black&family=Bungee&family=League+Spartan:wght@800&display=swap">
<style>
  :root {
    --plum: #8c006c;
    --lime: #86af00;
    --ink: #0a0a0a;
    --paper: #ffffff;
  }
  html, body {
    margin: 0;
    width: 1200px;
    height: 1000px;
    overflow: hidden;
    background: var(--paper);
  }
  .poster {
    position: absolute;
    left: 267px;
    top: 100px;
    width: 666px;
    height: 800px;
    background: var(--paper);
  }
  .poster svg { display: block; isolation: isolate; }
  .word-mini { font-family: "Bungee", sans-serif; fill: var(--lime); mix-blend-mode: multiply; }
  .word-caps { font-family: "Anton", sans-serif; fill: var(--plum); }
  .word-green { font-family: "Archivo Black", sans-serif; fill: var(--lime); mix-blend-mode: multiply; }
  .word-slab { font-family: "Alfa Slab One", serif; fill: var(--plum); }
  .price-line { font-family: "League Spartan", sans-serif; font-weight: 800; fill: var(--ink); }
  .brand-name { font-family: "League Spartan", sans-serif; font-weight: 800; fill: var(--plum); }
  .brand-square { fill: var(--plum); }
  .manicule { fill: var(--plum); }
</style>
</head>
<body>
  <main class="poster">
    <svg width="666" height="800" viewBox="0 0 666 800" aria-label="Mini letterpress vending prints machine: 4 quarters for 1 surprise print">
      <text class="word-caps" x="43" y="261" font-size="155" textLength="578" lengthAdjust="spacingAndGlyphs">LETTER</text>
      <text class="word-caps" x="43" y="425" font-size="173" textLength="451" lengthAdjust="spacingAndGlyphs">PRESS</text>
      <text class="word-slab" x="43" y="589" font-size="140" textLength="436" lengthAdjust="spacingAndGlyphs">Prints</text>

      <text class="word-mini" x="43" y="140" font-size="133" textLength="181" lengthAdjust="spacingAndGlyphs">mini</text>
      <text class="word-green" x="87" y="513" font-size="175" textLength="534" lengthAdjust="spacingAndGlyphs">vending</text>
      <text class="word-green" x="97" y="679" font-size="173" textLength="524" lengthAdjust="spacingAndGlyphs">machine</text>

      <g class="brand">
        <rect class="brand-square" x="522" y="282" width="84" height="84"/>
        <text class="brand-name" x="510" y="410" font-size="26" textLength="110" lengthAdjust="spacingAndGlyphs">Quillmark</text>
      </g>

      <text class="price-line" x="74" y="720" font-size="38" textLength="193" lengthAdjust="spacingAndGlyphs">4 Quarters</text>
      <rect class="manicule" x="256" y="716" width="60" height="30" rx="13" role="img" aria-label="Pointing hand manicule illustration"/>
      <text class="price-line" x="321" y="751" font-size="38" textLength="269" lengthAdjust="spacingAndGlyphs">1 Surprise Print</text>
    </svg>
  </main>
</body>
</html>
```